Etiketten-Design für Honig
Zielgruppe
Selbst: Imker
Zielgruppe: Privatkunden/ Verbraucher
Aufgabenstellung
Ich verkaufe Honig. Design soll hip sein. Auf dem Logo soll mein Name meine Anschrift stehen, aber nicht dominant. Es muss ersichtlich sein, dass es Honig ist, der verkauft wird. Ideal wäre, wenn zum Ankreuzen je ein Feld mit der Bezeichnung Waldhonig bzw. Blütenhonig stünde.
Ich benötige ein Lehrfeld mit der Kennzeichnung „Mindestens haltbar bis“
Gewichtsangabe Fixfeld mit 500 g.
Format: ca.9,5 x 5,5 cm

```html
<!DOCTYPE html>
<html lang="de">
<head>
<meta charset="UTF-8">
<title>Waldhonig Etikett</title>
<link rel="stylesheet" href="https://fonts.googleapis.com/css2?family=Josefin+Sans:wght@300;400&display=swap">
<style>
  :root {
    --canvas-bg: #efece7;
    --label-bg: #ffffff;
    --label-edge: #e2ddd6;
    --ink: #2b2724;
    --rule: #cfc6bc;
    --sketch-dark: #7a5a42;
    --sketch-light: #e9dfd4;
  }
  html, body {
    margin: 0;
    padding: 0;
    width: 1200px;
    height: 1200px;
    overflow: hidden;
    background: var(--canvas-bg);
  }
  .canvas {
    position: relative;
    width: 1200px;
    height: 1200px;
  }
  /* 9.5 x 5.5 cm label format */
  .honey-label {
    position: absolute;
    left: 50px;
    top: 282px;
    width: 1100px;
    height: 637px;
    background: var(--label-bg);
    border: 1px solid var(--label-edge);
    box-sizing: border-box;
    font-family: "Josefin Sans", sans-serif;
    color: var(--ink);
  }
  .scene-illustration {
    position: absolute;
    left: 379px;
    top: 36px;
    width: 340px;
    height: 250px;
    background: radial-gradient(ellipse at 50% 55%, var(--sketch-dark) 0%, #b89b84 38%, var(--sketch-light) 68%, var(--label-bg) 100%);
    opacity: 0.55;
  }
  .product-name {
    position: absolute;
    left: 0;
    right: 0;
    top: 304px;
    margin: 0;
    text-align: center;
    font-weight: 300;
    font-size: 96px;
    line-height: 1;
    letter-spacing: 0.01em;
  }
  .beekeeper-address {
    position: absolute;
    left: 0;
    right: 0;
    top: 412px;
    margin: 0;
    text-align: center;
    font-weight: 400;
    font-size: 38px;
    line-height: 1;
    letter-spacing: 0.14em;
  }
  .info-band {
    position: absolute;
    left: 60px;
    right: 60px;
    top: 482px;
    height: 120px;
    border-top: 1px solid var(--rule);
    display: flex;
    align-items: center;
    justify-content: space-between;
  }
  .honey-types {
    display: flex;
    flex-direction: column;
    gap: 14px;
  }
  .honey-type {
    display: flex;
    align-items: center;
    gap: 14px;
    font-size: 28px;
    font-weight: 400;
    line-height: 1;
  }
  .tick-box {
    width: 26px;
    height: 26px;
    border: 2px solid var(--ink);
    box-sizing: border-box;
  }
  .best-before {
    display: flex;
    flex-direction: column;
    gap: 30px;
    font-size: 24px;
    font-weight: 400;
    letter-spacing: 0.04em;
  }
  .best-before-line {
    width: 300px;
    border-bottom: 2px solid var(--ink);
  }
  .net-weight {
    font-size: 52px;
    font-weight: 300;
    letter-spacing: 0.04em;
    line-height: 1;
  }
</style>
</head>
<body>
  <main class="canvas">
    <section class="honey-label">
      <div class="scene-illustration" role="img" aria-label="Zeichnung einer Berglandschaft mit Almhütten, Tannen und einem hölzernen Bienenstock im Vordergrund"></div>
      <h1 class="product-name">WALDHONIG</h1>
      <p class="beekeeper-address">Address</p>
      <div class="info-band">
        <div class="honey-types">
          <div class="honey-type"><span class="tick-box"></span>Waldhonig</div>
          <div class="honey-type"><span class="tick-box"></span>Blütenhonig</div>
        </div>
        <div class="best-before">
          <span>Mindestens haltbar bis</span>
          <span class="best-before-line"></span>
        </div>
        <div class="net-weight">500 g</div>
      </div>
    </section>
  </main>
</body>
</html>
```